trailbuzz.example - youth/backpackers Adventure Travel contact site

Landing Page: Logo, @RoamQuestOutfitters, Australia | New Zealand | Fiji | South East Asia, Start Button, a Rotating carousel of supplier logos, ©Trail Buzz Journeys, Terms and Conditions link, Contact Us page link, social media/contact icons.
Start Button: Takes you to destinations selection Map - Hover over effect with selectable Countries, states, regions, and next & back buttons.
Next Button: Takes you to Activities - Selectable Buttons for Sky Diving, Sailing, Whitewater Rafting, Bungee jumping, camping, hiking, Surfing, Jet Boating, kayaking, canyoning, National Parks, Scuba Diving, Snorkeling and beaches etc., Tandem Hand gliding, with a typable "Have we missed anything you want to experience" area and back and next buttons.
Next Button: Takes you to extras - Selectable buttons for Bus Passes, Accommodation, Car Hire, Camper Hire and back and next buttons.
Next Button: Takes you to enter customer details: Name, Age, Phone, Email, How did you hear about us, Dietary requirement, start & end date, start & end location, Number of Travellers, Budget, anything else area, Submit for your custom adventure button. - All this information then gets emailed.

Target Market(s)

Backpacker/youth adventure travel

Industry/Entity Type

Travel Agent

Coding

Coded - Design and coding required

Number of Pages Required

3 page

Colors

Designer to choose colors to be used in the design.

Requirements
Must have
• Somewhere to be automatically synced Snaps profile pictures and videos.
• Full screen, scalable to any device size - 65% of our users use mobile devices.
• Wordpress
Nice to have
• Easy to add and remove selectable buttons
• If you can think of any special feature to add ;)
Should not have
• Basic contact form look

```html
<!DOCTYPE html>
<html lang="en">
<head>
<meta charset="utf-8">
<title>Trail Buzz Journeys – Adventure Travel Specialists</title>
<link href="https://fonts.googleapis.com/css2?family=Montserrat:wght@800&family=Jost:wght@300;400;500&display=swap" rel="stylesheet">
<style>
  :root {
    --sky-top: #0a0a0d;
    --sky-mid: #1c1412;
    --sky-low: #3b1e15;
    --rock: #4a2418;
    --rock-dark: #2a150f;
    --footer: #08080a;
    --white: #ffffff;
    --coral: #f0503f;
    --muted: rgba(255,255,255,0.55);
    --rule: rgba(255,255,255,0.35);
  }
  * { margin: 0; padding: 0; box-sizing: border-box; }
  html, body { width: 1200px; height: 918px; overflow: hidden; background: var(--sky-top); }
  .page {
    position: relative; width: 1200px; height: 918px; overflow: hidden;
    font-family: "Jost", sans-serif; color: var(--white);
    background: linear-gradient(180deg, var(--sky-top) 0%, var(--sky-mid) 38%, var(--sky-low) 72%, var(--sky-low) 100%);
  }
  .night-sky { position: absolute; inset: 0 0 94px 0; background: radial-gradient(ellipse 70% 30% at 55% 30%, rgba(120,100,90,0.18), transparent 70%); }
  .rock-band {
    position: absolute; left: 0; right: 0; top: 656px; height: 168px;
    background: linear-gradient(180deg, rgba(74,36,24,0) 0%, var(--rock) 35%, var(--rock-dark) 100%);
  }
  .menu-toggle { position: absolute; left: 50px; top: 49px; width: 19px; height: 16px; display: flex; flex-direction: column; justify-content: space-between; }
  .menu-toggle span { display: block; height: 3px; border-radius: 2px; background: var(--white); }
  .social { position: absolute; right: 58px; top: 48px; display: flex; align-items: center; gap: 16px; font-size: 12px; letter-spacing: 0.5px; }
  .social svg { display: block; }
  .brand {
    position: absolute; left: 0; right: 0; top: 132px; text-align: center;
    font-family: "Jost", sans-serif; font-weight: 500; font-size: 34px; letter-spacing: 2px; color: var(--coral);
    display: flex; justify-content: center; align-items: center; gap: 12px;
  }
  .brand-dot { width: 14px; height: 14px; border-radius: 50%; background: var(--coral); }
  .headline {
    position: absolute; left: 0; right: 0; top: 268px; text-align: center; white-space: nowrap;
    font-family: "Montserrat", sans-serif; font-weight: 800; font-size: 38px; letter-spacing: 3.5px; word-spacing: 8px;
  }
  .tagline {
    position: absolute; left: 0; right: 0; top: 333px; text-align: center;
    font-weight: 300; font-size: 26px; letter-spacing: 0.5px; color: var(--coral); text-transform: uppercase;
  }
  .destinations { position: absolute; left: 0; top: 0; width: 1200px; height: 918px; pointer-events: none; }
  .region-map { position: absolute; background: linear-gradient(180deg, #f4f4f4, #dcdcdc); border-radius: 40% 45% 35% 50%; opacity: 0.95; }
  .dest-label { position: absolute; top: 508px; transform: translateX(-50%); font-size: 19px; letter-spacing: 1px; line-height: 24px; white-space: nowrap; }
  .dest-label.is-active { color: var(--coral); }
  .start-btn {
    position: absolute; left: 408px; top: 566px; width: 384px; height: 52px; border-radius: 26px;
    background: var(--coral); display: flex; align-items: center; padding-left: 37px;
    font-weight: 500; font-size: 20px; letter-spacing: 1.2px; color: var(--white); text-decoration: none; white-space: nowrap;
  }
  .start-btn .arrow { position: absolute; right: 1px; top: 1px; width: 50px; height: 50px; border-radius: 50%; background: var(--white); display: flex; align-items: center; justify-content: center; }
  .rule { position: absolute; left: 168px; width: 864px; height: 1px; background: var(--rule); }
  .partners { position: absolute; left: 0; right: 0; top: 690px; height: 76px; }
  .partner { position: absolute; top: 22px; line-height: 36px; transform: translateX(-50%); font-size: 26px; font-weight: 400; letter-spacing: 1px; color: var(--muted); white-space: nowrap; }
  .carousel-arrow { position: absolute; top: 720px; }
  .site-footer { position: absolute; left: 0; right: 0; bottom: 0; height: 94px; background: var(--footer); text-align: center; }
  .copyright { position: absolute; left: 0; right: 0; top: 17px; font-size: 14px; letter-spacing: 1px; }
  .legal { position: absolute; left: 0; right: 0; top: 57px; display: flex; justify-content: center; font-size: 11px; letter-spacing: 0.8px; }
  .legal a { color: var(--white); text-decoration: none; padding: 0 10px; line-height: 16px; }
  .legal a + a { border-left: 1px solid var(--white); }
</style>
</head>
<body>
<main class="page">
  <div class="night-sky" role="img" aria-label="Starry night sky with the Milky Way"></div>
  <div class="rock-band" role="img" aria-label="Rocky outcrop silhouetted at dusk"></div>

  <div class="menu-toggle" aria-label="Menu"><span></span><span></span><span></span></div>

  <nav class="social">
    <span>Chatter</span>
    <span>Reels</span>
    <span>Snaps</span>
    <svg width="22" height="16" viewBox="0 0 22 16" aria-label="Email"><rect x="0" y="0" width="22" height="16" rx="2" fill="#fff"/><path d="M1 2 L11 9 L21 2" fill="none" stroke="#0a0a0d" stroke-width="2"/></svg>
  </nav>

  <div class="brand"><span class="brand-dot"></span>Trail Buzz Journeys</div>

  <h1 class="headline">ADVENTURE TRAVEL SPECIALISTS</h1>
  <p class="tagline">Discover travel that stirs your soul</p>

  <section class="destinations">
    <svg width="1200" height="918" style="position:absolute;left:0;top:0">
      <g stroke="#fff" stroke-width="1.5" fill="none">
        <polyline points="247,520 210,520 210,389 990,389 990,520 903,520"/>
        <line x1="333" y1="520" x2="364" y2="520"/>
        <line x1="485" y1="520" x2="540" y2="520"/>
        <line x1="568" y1="520" x2="632" y2="520"/>
        <line x1="770" y1="520" x2="864" y2="520"/>
      </g>
    </svg>
    <div class="region-map" style="left:248px;top:408px;width:94px;height:86px" role="img" aria-label="Map of Australia"></div>
    <div class="region-map" style="left:408px;top:406px;width:48px;height:90px;border-radius:40%" role="img" aria-label="Map of New Zealand"></div>
    <div class="region-map" style="left:520px;top:410px;width:76px;height:60px;border-radius:50% 30% 50% 40%" role="img" aria-label="Map of Fiji"></div>
    <div class="region-map" style="left:664px;top:405px;width:84px;height:90px" role="img" aria-label="Map of South East Asia"></div>
    <div class="region-map" style="left:810px;top:405px;width:142px;height:88px;border-radius:30% 50% 45% 40%" role="img" aria-label="Map of Bali"></div>
    <span class="dest-label" style="left:290px">Australia</span>
    <span class="dest-label is-active" style="left:424px">New Zealand</span>
    <span class="dest-label" style="left:555px">Fiji</span>
    <span class="dest-label" style="left:701px">South East Asia</span>
    <span class="dest-label" style="left:883px">Bali</span>
  </section>

  <a class="start-btn" href="#">START NEXT ADVENTURE
    <span class="arrow"><svg width="14" height="20" viewBox="0 0 14 20"><polyline points="3,2 11,10 3,18" fill="none" stroke="#f0503f" stroke-width="3" stroke-linecap="round" stroke-linejoin="round"/></svg></span>
  </a>

  <div class="rule" style="top:650px"></div>

  <svg class="carousel-arrow" style="left:85px" width="10" height="16" viewBox="0 0 10 16"><polyline points="8,2 2,8 8,14" fill="none" stroke="#fff" stroke-width="2"/></svg>
  <div class="partners">
    <span class="partner" style="left:232px">NORTHVALE</span>
    <span class="partner" style="left:418px">Keystone</span>
    <span class="partner" style="left:590px;font-size:18px">FERNLEAF STAYS</span>
    <span class="partner" style="left:794px">HARBOURLINE</span>
    <span class="partner" style="left:982px">metrowise</span>
  </div>
  <svg class="carousel-arrow" style="left:1106px" width="10" height="16" viewBox="0 0 10 16"><polyline points="2,2 8,8 2,14" fill="none" stroke="#fff" stroke-width="2"/></svg>

  <div class="rule" style="top:792px"></div>

  <footer class="site-footer">
    <p class="copyright">© COPYRIGHT 2017 @ROAMQUESTOUTFITTERS</p>
    <nav class="legal">
      <a href="#">CONTACT US</a>
      <a href="#">TERMS AND CONDITIONS</a>
      <a href="#">PRIVACY POLICY</a>
    </nav>
  </footer>
</main>
</body>
</html>
```